Real Estate Agent needs business card design

We have logo designed already, want to have business card designed. Very interested in those smaller size business card as they look very trendy. Business name is called VORENDA REALTY

```html
<!DOCTYPE html>
<html lang="en">
<head>
<meta charset="UTF-8">
<title>Vorenda Realty – Business Card</title>
<link href="https://fonts.googleapis.com/css2?family=Oswald:wght@500&family=Lora:wght@400;500&display=swap" rel="stylesheet">
<style>
  :root {
    --gold: #cba46d;
    --ink: #111111;
    --paper: #ffffff;
    --edge: #8a8a8a;
  }
  * { margin: 0; padding: 0; box-sizing: border-box; }
  html, body {
    width: 1200px;
    height: 1200px;
    overflow: hidden;
    background: var(--paper);
  }
  .canvas {
    position: relative;
    width: 1200px;
    height: 1200px;
    background: var(--paper);
  }

  /* Front of card */
  .card-front {
    position: absolute;
    left: 190px;
    top: 210px;
    width: 820px;
    height: 327px;
    background: var(--gold);
  }
  .front-brand {
    position: absolute;
    left: 24px;
    bottom: 26px;
    display: flex;
    align-items: center;
    gap: 14px;
    font-family: "Lora", serif;
    font-weight: 500;
    font-size: 34px;
    letter-spacing: 3px;
    color: var(--paper);
  }
  .front-brand .brand-square {
    width: 22px;
    height: 22px;
    background: var(--paper);
  }

  /* Back of card */
  .card-back {
    position: absolute;
    left: 190px;
    top: 665px;
    width: 820px;
    height: 327px;
    background: var(--paper);
    border: 1px solid var(--edge);
  }
  .back-brand {
    position: absolute;
    left: 38px;
    top: 30px;
    height: 140px;
    display: flex;
    align-items: center;
    gap: 10px;
  }
  .back-brand .brand-square {
    width: 18px;
    height: 18px;
    background: var(--gold);
  }
  .back-brand .brand-name {
    writing-mode: vertical-rl;
    transform: rotate(180deg);
    font-family: "Lora", serif;
    font-weight: 400;
    font-size: 17px;
    letter-spacing: 1px;
    color: var(--ink);
  }
  .divider {
    position: absolute;
    left: 125px;
    top: 31px;
    width: 3px;
    height: 262px;
    background: var(--gold);
  }
  .details {
    position: absolute;
    left: 153px;
    top: 136px;
  }
  .agent-name {
    font-family: "Oswald", sans-serif;
    font-weight: 500;
    font-size: 31px;
    letter-spacing: 3.5px;
    color: var(--ink);
    line-height: 1;
    margin-bottom: 22px;
  }
  .agent-title,
  .contact-line {
    font-family: "Lora", serif;
    font-size: 17px;
    letter-spacing: 1.4px;
    line-height: 29px;
    color: var(--ink);
  }
  .agent-title {
    color: var(--gold);
    font-weight: 500;
  }
</style>
</head>
<body>
  <div class="canvas">
    <section class="card-front">
      <div class="front-brand">
        <span class="brand-square"></span>
        <span class="brand-name">VORENDA REALTY</span>
      </div>
    </section>

    <section class="card-back">
      <div class="back-brand">
        <span class="brand-square"></span>
        <span class="brand-name">VORENDA REALTY</span>
      </div>
      <div class="divider"></div>
      <div class="details">
        <h1 class="agent-name">SIENNA HARTLEY</h1>
        <p class="agent-title">Senior Property Consultant</p>
        <p class="contact-line">0412 555 390</p>
        <p class="contact-line">7C, 148 Linden Avenue, Marlow Bay, NSW 2199</p>
        <p class="contact-line">www.vorendarealty.com.au</p>
      </div>
    </section>
  </div>
</body>
</html>
```